Launching a new real estate agency in Monaco

Hello, I am opening a new real estate agency in Monaco. For the purpose of my activity, in order to be known quickly among a fierce competition I need an advertising campaign that will be broadcast in local magazines, newspapers, paper board, etc.

You will find example of pictures of Monaco on which I have the rights and my logo. You can always pick other images that I can buy if the price is reasonable for a commercial use (<200 $)

Please respect the color code.

I wish you good luck and look forward to give you my feedbacks

Reason: Only few projects posted were respecting the brief and of quality. Hoping to receive more in coming days

Target Market(s)

International high-end clientele of all ages, all genders.

Industry/Entity Type

Real Estate Agent

Font styles to use
Serif

Requirements
Must have
• 1/ My logo
• 2/ This message "Un nouveau regard sur l'immobilier" means in English a fresh look at real estate or new eyes on real-estate.
• 3/ My address: 14 rue des Orvilles, Passage Marcellin, 98 000 Monaco
• 4/ Phone number: +377.93.48.25.71
• 5/ Website: www.brunor-agency.com.
• 6/ Format: Files should be easily adjustable but I'd like a vertical display to fit easily in Magazines, Poster and billboard. So please work in high resolution !
Nice to have
• Please think about your design in accordance with the message I want to display.
Should not have
• A simple poster with a picture of Monaco that does not take into consideration the message of the advertisement, "Un nouveau regard sur l'immobilier" which means in english, new eyes on real-estate or a new look at real-estate, or new vision at real-estate.

```html
<!DOCTYPE html>
<html lang="fr">
<head>
<meta charset="utf-8">
<title>Brunor Agency – Un nouveau regard sur l'immobilier</title>
<link rel="stylesheet" href="https://fonts.googleapis.com/css2?family=Abril+Fatface&family=Cinzel:wght@400&family=Montserrat:wght@400&display=swap">
<style>
  :root {
    --cream: #fcf8ee;
    --salmon: #e0967e;
    --ink-grey: #5f5f5f;
  }
  * { margin: 0; padding: 0; box-sizing: border-box; }
  html, body { width: 954px; height: 1200px; overflow: hidden; background: var(--cream); }
  .poster {
    position: relative;
    width: 954px;
    height: 1200px;
    background: var(--cream);
    overflow: hidden;
  }
  .headline {
    position: absolute;
    top: 176px;
    left: 0;
    width: 100%;
    text-align: center;
    font-family: "Abril Fatface", serif;
    font-weight: 400;
    font-size: 68px;
    line-height: 80px;
    letter-spacing: 5px;
    color: var(--salmon);
    text-transform: uppercase;
  }
  .contact {
    position: absolute;
    top: 357px;
    left: 0;
    width: 100%;
    text-align: center;
    font-family: "Cinzel", serif;
    font-style: normal;
    font-size: 13px;
    letter-spacing: 1.8px;
    color: var(--ink-grey);
    line-height: 27px;
  }
  .brand {
    position: absolute;
    top: 503px;
    left: 0;
    width: 100%;
    display: flex;
    justify-content: center;
    align-items: center;
    gap: 16px;
  }
  .brand-mark {
    width: 50px;
    height: 50px;
    background: var(--salmon);
  }
  .brand-name {
    font-family: "Abril Fatface", serif;
    font-size: 46px;
    letter-spacing: 3px;
    color: var(--salmon);
    line-height: 1;
  }
  .website {
    position: absolute;
    top: 587px;
    left: 0;
    width: 100%;
    text-align: center;
    font-family: "Montserrat", sans-serif;
    font-size: 18px;
    letter-spacing: 4px;
    color: var(--ink-grey);
    text-transform: uppercase;
  }
  .harbour {
    position: absolute;
    left: 0;
    top: 540px;
    width: 954px;
    height: 660px;
  }
</style>
</head>
<body>
  <main class="poster">
    <h1 class="headline">Un nouveau regard<br>sur l'immobilier</h1>

    <address class="contact">
      14 rue des Orvilles, Passage Marcellin, 98 000 Monaco<br>
      +377.93.48.25.71
    </address>

    <div class="brand">
      <span class="brand-mark"></span>
      <span class="brand-name">BRUNOR AGENCY</span>
    </div>

    <p class="website">www.brunor-agency.com</p>

    <svg class="harbour" viewBox="0 0 954 660" role="img" aria-label="Evening aerial view of a Monaco harbour with lit apartment buildings along the sea and moored yachts">
      <defs>
        <clipPath id="harbour-shape">
          <path d="M0 84 C 240 130, 520 140, 700 96 C 800 70, 880 40, 954 16 L954 660 L0 660 Z"/>
        </clipPath>
        <linearGradient id="harbour-base" x1="0" y1="0" x2="0" y2="1">
          <stop offset="0" stop-color="#efd2b8"/>
          <stop offset="0.2" stop-color="#b7a49a"/>
          <stop offset="0.26" stop-color="#2c5c91"/>
          <stop offset="0.45" stop-color="#23548a"/>
          <stop offset="0.65" stop-color="#1b3f68"/>
          <stop offset="1" stop-color="#0c2038"/>
        </linearGradient>
        <radialGradient id="harbour-glow" cx="0.58" cy="0.5" r="0.6" fx="0.55" fy="0.52">
          <stop offset="0" stop-color="#f0b062" stop-opacity="1"/>
          <stop offset="0.35" stop-color="#d58f52" stop-opacity="0.95"/>
          <stop offset="0.65" stop-color="#9c6440" stop-opacity="0.55"/>
          <stop offset="1" stop-color="#9c6440" stop-opacity="0"/>
        </radialGradient>
        <linearGradient id="harbour-dusk" x1="0" y1="0" x2="1" y2="0">
          <stop offset="0" stop-color="#1f5590" stop-opacity="0.85"/>
          <stop offset="0.18" stop-color="#1f5590" stop-opacity="0"/>
          <stop offset="0.82" stop-color="#10284a" stop-opacity="0"/>
          <stop offset="1" stop-color="#10284a" stop-opacity="0.5"/>
        </linearGradient>
      </defs>
      <g clip-path="url(#harbour-shape)">
        <rect width="954" height="660" fill="url(#harbour-base)"/>
        <ellipse cx="560" cy="400" rx="600" ry="230" fill="url(#harbour-glow)"/>
        <rect width="954" height="660" fill="url(#harbour-dusk)"/>
      </g>
    </svg>
  </main>
</body>
</html>
```